Unique Business Card Design

Unique Business Card design for our orthotic and prosthetic company. Our logo is on our website, color is light blue. Unique shape (artificial leg shaped, vertical, etc..) preferred. Logo, business name, individual name and basic demographics needed.

Industry/Entity Type

Business

Contact Information for Business Card

Logo, Industry, Phone # Logo, "Prosthetic & Orthotic Services" Place to add individual name and contact info

Colors
cee9f5

Requirements
Must have
• The icon must be there, placement of "Prosthetic & Orthotic Services" can be moved
Nice to have
• Like the mix of light blue, and a little darker blue. One design included the icons from my website which was a nice touch

```html
<!DOCTYPE html>
<html lang="en">
<head>
<meta charset="utf-8">
<title>Limbworks Co – Business Card</title>
<link rel="stylesheet" href="https://fonts.googleapis.com/css2?family=Source+Sans+3:wght@400;600;700&family=Crimson+Text:ital@1&display=swap">
<style>
  :root {
    --stage: #141414;
    --card-light: #d0e9f5;
    --brand-blue: #0f6cc6;
    --brand-deep: #0d5fbd;
    --brand-pattern: #0b57ae;
    --ink: #2b2b2b;
    --ink-strong: #111;
    --white: #ffffff;
  }
  * { box-sizing: border-box; margin: 0; padding: 0; }
  html, body { width: 1200px; height: 900px; overflow: hidden; }
  body {
    background: var(--stage);
    font-family: "Source Sans 3", "Myriad Pro", sans-serif;
    position: relative;
  }
  .card {
    position: absolute;
    top: 306px;
    width: 439px;
    height: 271px;
    border-radius: 10px;
    overflow: hidden;
  }
  .card--front { left: 150px; background: var(--card-light); }
  .card--back { left: 609px; }

  .brand-disc {
    position: absolute;
    left: 43px; top: 65px;
    width: 141px; height: 141px;
    border-radius: 50%;
    background: var(--brand-blue);
    display: flex; align-items: center; justify-content: center;
  }
  .brand-disc__name {
    color: var(--white);
    font-weight: 700;
    font-size: 15px;
    letter-spacing: 0.5px;
  }

  .contact { position: absolute; left: 231px; top: 52px; }
  .contact__name { color: var(--brand-blue); font-weight: 700; font-size: 19px; line-height: 1; }
  .contact__title { color: var(--ink); font-size: 12.5px; margin: 3px 0 0 2px; }
  .contact__list { list-style: none; margin-top: 24px; }
  .contact__item { display: flex; align-items: center; gap: 5px; color: var(--ink); font-size: 12.5px; line-height: 16px; }
  .contact__item--phone { color: var(--ink-strong); font-weight: 600; font-size: 14.5px; margin-bottom: 4px; }
  .contact__item svg { width: 9px; height: 9px; fill: var(--brand-blue); flex: none; }
  .contact__address { color: var(--ink); font-size: 12.5px; line-height: 16px; margin-top: 13px; }

  .back-field {
    position: absolute; inset: 0;
    background: radial-gradient(circle at 50% 50%, var(--brand-deep), var(--brand-pattern));
  }
  .back-disc {
    position: absolute;
    left: 67px; top: 95px;
    width: 81px; height: 81px;
    border-radius: 50%;
    background: var(--white);
  }
  .wordmark { position: absolute; left: 168px; top: 106px; width: 204px; text-align: center; color: var(--white); }
  .wordmark__name {
    font-weight: 600; font-size: 25px; line-height: 28px; letter-spacing: 0.3px;
    padding-bottom: 4px; border-bottom: 2px solid var(--white);
  }
  .wordmark__tagline {
    font-family: "Crimson Text", Georgia, serif; font-style: italic;
    font-size: 13.5px; margin-top: 4px;
  }
  .back-web {
    position: absolute; left: 0; right: 0; top: 220px;
    text-align: center; color: var(--white); font-size: 13px;
  }
</style>
</head>
<body>
  <section class="card card--front" aria-label="Business card front">
    <div class="brand-disc"><span class="brand-disc__name">LIMBWORKS CO</span></div>
    <div class="contact">
      <p class="contact__name">Daniel Reyes</p>
      <p class="contact__title">Managing Director</p>
      <ul class="contact__list">
        <li class="contact__item contact__item--phone">
          <svg viewBox="0 0 24 24" aria-hidden="true"><path d="M6.6 10.8a15.1 15.1 0 0 0 6.6 6.6l2.2-2.2c.3-.3.7-.4 1-.2 1.1.4 2.3.6 3.6.6.6 0 1 .4 1 1V20c0 .6-.4 1-1 1A17 17 0 0 1 3 4c0-.6.4-1 1-1h3.5c.6 0 1 .4 1 1 0 1.3.2 2.5.6 3.6.1.3 0 .7-.2 1z"/></svg>
          (555) 204-3860
        </li>
        <li class="contact__item">
          <svg viewBox="0 0 24 24" aria-hidden="true"><path d="M2 5h20v14H2z M2 5l10 8 10-8" /></svg>
          hello@limbworksco.com
        </li>
        <li class="contact__item">
          <svg viewBox="0 0 24 24" aria-hidden="true"><path d="M10 14a4 4 0 0 1 0-5.7l3-3a4 4 0 0 1 5.7 5.7l-1.5 1.5-1.4-1.4 1.5-1.5a2 2 0 0 0-2.9-2.9l-3 3a2 2 0 0 0 0 2.9zM14 10a4 4 0 0 1 0 5.7l-3 3a4 4 0 0 1-5.7-5.7l1.5-1.5 1.4 1.4-1.5 1.5a2 2 0 0 0 2.9 2.9l3-3a2 2 0 0 0 0-2.9z"/></svg>
          www.limbworksco.com
        </li>
      </ul>
      <p class="contact__address">1234, Address Goes Here<br>Country Name, 123456</p>
    </div>
  </section>

  <section class="card card--back" aria-label="Business card back">
    <div class="back-field" role="img" aria-label="Faint repeating brand pattern on blue"></div>
    <div class="back-disc"></div>
    <div class="wordmark">
      <p class="wordmark__name">LIMBWORKS CO</p>
      <p class="wordmark__tagline">Prosthetic &amp; Orthotic Services</p>
    </div>
    <p class="back-web">www.limbworksco.com</p>
  </section>
</body>
</html>
```